Electronic Time-sheet for phones

I need a time-sheet that can be accessed on the phone, be completed, then have the ability to electronically sign. The time sheet needs to be used two fold for supervision to verify hours and quantities and also for the client to be able to electronically sign. The time-sheet should be daily or weekly if we can get the data to fit. We are trying to streamline field supervisors having to log on to a computer to access a server just to do time-sheets. We need it to be user friendly. We need to have two places to have electronic signatures. One for supervisor or authorized representative and the other for the client to sign.

Target Market(s)

Industrial clients

Industry/Entity Type

Oil And Gas

Requirements
Must have
• hours, quantities, project name, location, signature line etc
Nice to have
• n/a
Should not have
• n/a

```html
<!DOCTYPE html>
<html lang="en">
<head>
<meta charset="UTF-8">
<title>Formans Daily Time Sheets</title>
<link href="https://fonts.googleapis.com/css2?family=Montserrat:ital,wght@0,500;0,600;0,700;1,400&display=swap" rel="stylesheet">
<style>
  :root {
    --brand-blue: #2c5bfb;
    --page-bg: #eef1fc;
    --card-bg: #ffffff;
    --tab-blue: #7890f6;
    --icon-blue: #6d88f2;
    --name-grey: #6b6b6b;
    --meta-grey: #7d7d7d;
    --white: #ffffff;
    --photo-dark: #2a2624;
    --photo-mid: #7a6a5e;
  }
  * { margin: 0; padding: 0; box-sizing: border-box; }
  html, body { width: 675px; height: 1200px; overflow: hidden; }
  body {
    position: relative;
    background: var(--page-bg);
    font-family: "Montserrat", sans-serif;
  }
  .app-header {
    position: absolute; left: 0; top: 0;
    width: 675px; height: 162px;
    background: var(--brand-blue);
    color: var(--white);
  }
  .status-bar {
    position: absolute; left: 0; top: 0; width: 100%; height: 70px;
  }
  .status-time {
    position: absolute; left: 54px; top: 20px;
    font-size: 25px; font-weight: 600;
  }
  .status-icons { position: absolute; right: 36px; top: 24px; }
  .screen-title {
    position: absolute; left: 0; right: 0; top: 104px;
    text-align: center;
    font-size: 29px; font-weight: 700; letter-spacing: 0.2px;
  }
  .menu-button { position: absolute; left: 611px; top: 110px; }

  .employee-list {
    position: absolute; left: 31px; top: 189px;
    width: 610px;
    display: flex; flex-direction: column; gap: 18px;
  }
  .employee-card { position: relative; height: 173px; }
  .employee-info {
    position: absolute; left: 0; top: 0;
    width: 610px; height: 122px;
    background: var(--card-bg);
    border-radius: 11px 11px 0 11px;
  }
  .employee-photo {
    position: absolute; left: 0; top: 0;
    width: 122px; height: 122px;
    border-radius: 11px;
    background: radial-gradient(circle at 50% 40%, var(--photo-mid) 0%, #4a3f38 45%, var(--photo-dark) 80%);
  }
  .employee-name {
    position: absolute; left: 151px; top: 28px;
    display: flex; align-items: center; gap: 14px;
    font-size: 25px; font-weight: 600; color: var(--name-grey);
  }
  .employee-meta {
    position: absolute; left: 194px; top: 71px;
    font-size: 19px; font-style: italic; font-weight: 400;
    color: var(--meta-grey);
    white-space: nowrap;
  }
  .employee-meta span + span { margin-left: 22px; }
  .more-tab {
    position: absolute; right: 0; top: 122px;
    width: 126px; height: 51px;
  }
  .more-tab svg { position: absolute; inset: 0; }
  .more-label {
    position: absolute; right: 28px; top: 15px;
    font-size: 17px; font-weight: 600; color: var(--white);
  }
</style>
</head>
<body>
  <header class="app-header">
    <div class="status-bar">
      <span class="status-time">9:41</span>
      <svg class="status-icons" width="122" height="22" viewBox="0 0 122 22">
        <g fill="#ffffff">
          <rect x="0" y="14" width="5" height="7" rx="1"/>
          <rect x="8" y="10" width="5" height="11" rx="1"/>
          <rect x="16" y="5" width="5" height="16" rx="1"/>
          <rect x="24" y="0" width="5" height="21" rx="1"/>
          <path d="M44 19 l5 -5 a7 7 0 0 0 -10 0 z"/>
          <path d="M36 11 a12 12 0 0 1 16 0 l-2.5 2.5 a8.5 8.5 0 0 0 -11 0 z"/>
          <path d="M32 7 a18 18 0 0 1 24 0 l-2.5 2.5 a14.5 14.5 0 0 0 -19 0 z"/>
          <rect x="78" y="2" width="38" height="18" rx="5" fill="none" stroke="#ffffff" stroke-width="2" opacity="0.6"/>
          <rect x="81" y="5" width="32" height="12" rx="3"/>
          <rect x="118" y="8" width="3" height="6" rx="1" opacity="0.6"/>
        </g>
      </svg>
    </div>
    <h1 class="screen-title">Formans Daily Time Sheets</h1>
    <svg class="menu-button" width="30" height="24" viewBox="0 0 30 24" aria-label="Menu">
      <g stroke="#ffffff" stroke-width="3" stroke-linecap="round">
        <line x1="2" y1="3" x2="28" y2="3"/>
        <line x1="2" y1="12" x2="22" y2="12"/>
        <line x1="2" y1="21" x2="28" y2="21"/>
      </g>
    </svg>
  </header>

  <main class="employee-list">
    <article class="employee-card">
      <div class="employee-info">
        <div class="employee-photo" role="img" aria-label="Employee portrait photo"></div>
        <div class="employee-name">
          <svg width="29" height="27" viewBox="0 0 29 27"><g fill="var(--icon-blue)"><circle cx="14.5" cy="7" r="7"/><path d="M0 27 v-3 c0-5 6-8 14.5-8 s14.5 3 14.5 8 v3 z"/></g></svg>
          John Doe
        </div>
        <p class="employee-meta"><span>Class: JE-A</span><span>Emp-No: 1547</span></p>
      </div>
      <div class="more-tab">
        <svg width="126" height="51" viewBox="0 0 126 51"><path d="M0 0 H126 V44 a7 7 0 0 1 -7 7 H18 Z" fill="var(--tab-blue)"/></svg>
        <span class="more-label">MORE</span>
      </div>
    </article>

    <article class="employee-card">
      <div class="employee-info">
        <div class="employee-photo" role="img" aria-label="Employee portrait photo"></div>
        <div class="employee-name">
          <svg width="29" height="27" viewBox="0 0 29 27"><g fill="var(--icon-blue)"><circle cx="14.5" cy="7" r="7"/><path d="M0 27 v-3 c0-5 6-8 14.5-8 s14.5 3 14.5 8 v3 z"/></g></svg>
          John Doe
        </div>
        <p class="employee-meta"><span>Class: JE-A</span><span>Emp-No: 1547</span></p>
      </div>
      <div class="more-tab">
        <svg width="126" height="51" viewBox="0 0 126 51"><path d="M0 0 H126 V44 a7 7 0 0 1 -7 7 H18 Z" fill="var(--tab-blue)"/></svg>
        <span class="more-label">MORE</span>
      </div>
    </article>

    <article class="employee-card">
      <div class="employee-info">
        <div class="employee-photo" role="img" aria-label="Employee portrait photo"></div>
        <div class="employee-name">
          <svg width="29" height="27" viewBox="0 0 29 27"><g fill="var(--icon-blue)"><circle cx="14.5" cy="7" r="7"/><path d="M0 27 v-3 c0-5 6-8 14.5-8 s14.5 3 14.5 8 v3 z"/></g></svg>
          John Doe
        </div>
        <p class="employee-meta"><span>Class: JE-A</span><span>Emp-No: 1547</span></p>
      </div>
      <div class="more-tab">
        <svg width="126" height="51" viewBox="0 0 126 51"><path d="M0 0 H126 V44 a7 7 0 0 1 -7 7 H18 Z" fill="var(--tab-blue)"/></svg>
        <span class="more-label">MORE</span>
      </div>
    </article>

    <article class="employee-card">
      <div class="employee-info">
        <div class="employee-photo" role="img" aria-label="Employee portrait photo"></div>
        <div class="employee-name">
          <svg width="29" height="27" viewBox="0 0 29 27"><g fill="var(--icon-blue)"><circle cx="14.5" cy="7" r="7"/><path d="M0 27 v-3 c0-5 6-8 14.5-8 s14.5 3 14.5 8 v3 z"/></g></svg>
          John Doe
        </div>
        <p class="employee-meta"><span>Class: JE-A</span><span>Emp-No: 1547</span></p>
      </div>
      <div class="more-tab">
        <svg width="126" height="51" viewBox="0 0 126 51"><path d="M0 0 H126 V44 a7 7 0 0 1 -7 7 H18 Z" fill="var(--tab-blue)"/></svg>
        <span class="more-label">MORE</span>
      </div>
    </article>

    <article class="employee-card">
      <div class="employee-info">
        <div class="employee-photo" role="img" aria-label="Employee portrait photo"></div>
        <div class="employee-name">
          <svg width="29" height="27" viewBox="0 0 29 27"><g fill="var(--icon-blue)"><circle cx="14.5" cy="7" r="7"/><path d="M0 27 v-3 c0-5 6-8 14.5-8 s14.5 3 14.5 8 v3 z"/></g></svg>
          John Doe
        </div>
        <p class="employee-meta"><span>Class: JE-A</span><span>Emp-No: 1547</span></p>
      </div>
      <div class="more-tab">
        <svg width="126" height="51" viewBox="0 0 126 51"><path d="M0 0 H126 V44 a7 7 0 0 1 -7 7 H18 Z" fill="var(--tab-blue)"/></svg>
        <span class="more-label">MORE</span>
      </div>
    </article>

    <article class="employee-card">
      <div class="employee-info">
        <div class="employee-photo" role="img" aria-label="Employee portrait photo"></div>
        <div class="employee-name">
          <svg width="29" height="27" viewBox="0 0 29 27"><g fill="var(--icon-blue)"><circle cx="14.5" cy="7" r="7"/><path d="M0 27 v-3 c0-5 6-8 14.5-8 s14.5 3 14.5 8 v3 z"/></g></svg>
          John Doe
        </div>
        <p class="employee-meta"><span>Class: JE-A</span><span>Emp-No: 1547</span></p>
      </div>
      <div class="more-tab">
        <svg width="126" height="51" viewBox="0 0 126 51"><path d="M0 0 H126 V44 a7 7 0 0 1 -7 7 H18 Z" fill="var(--tab-blue)"/></svg>
        <span class="more-label">MORE</span>
      </div>
    </article>
  </main>
</body>
</html>
```